Velmoro Consulting Business

** Please add the content information from my old business card
1. I would like to see a two sided business card with both options with the 1st Option--Sketch Nest-new WHITE BACKGROUND LOGO
2 nd Option-Sketch Nest - new BLACK- Background Logo
3rd -Option a business card with my Photo on the card
Please add the new word to the card information:
EXECUTION
AS THE OWNER'S REP
WE AIM TO ACHIEVE YOUR
INFRASTRUCTURE VISION with
OUR SPECIALIZATION & EXECUTION in:

FUNDING Planning
BUSINESS Planning
INFRASTRUCTURE Planning
PROJECT Management
Since 2012
_____________________________________________________________________
I want to get spot uv raised printing. I was liking a a nice rich white linen paper stock with black writing & NOT A COLORED CARD other than a variety of white or black cards concept

```html
<!DOCTYPE html>
<html lang="en">
<head>
<meta charset="utf-8">
<title>Velmoro Consulting – Business Card</title>
<link rel="stylesheet" href="https://fonts.googleapis.com/css2?family=Arimo:ital,wght@0,400;0,700;1,700&display=swap">
<style>
  :root {
    --stage: #e6e6e4;
    --card-white: #ffffff;
    --brand-red: #e41d27;
    --brand-red-deep: #6e1218;
    --ink: #2a2a2e;
    --grey-text: #5d5d60;
    --white: #ffffff;
  }
  * { box-sizing: border-box; margin: 0; padding: 0; }
  html, body {
    width: 1200px; height: 801px; overflow: hidden;
    background: var(--stage);
    font-family: "Arimo", Arial, sans-serif;
  }
  .sheet { position: relative; width: 1200px; height: 801px; }
  .card {
    position: absolute; top: 245px;
    width: 540px; height: 310px;
    overflow: hidden;
  }

  /* Front */
  .card-front {
    left: 35px;
    background: var(--card-white);
    border-bottom: 4px solid var(--brand-red);
  }
  .brand-front {
    position: absolute; left: 300px; top: 56px;
    display: flex; align-items: center; gap: 10px;
  }
  .brand-mark { width: 14px; height: 14px; background: var(--brand-red); }
  .brand-name {
    font-weight: 700; font-size: 40px; color: var(--ink); letter-spacing: -0.5px;
  }
  .brand-tagline {
    position: absolute; left: 326px; top: 108px;
    font-size: 12px; letter-spacing: 9px; color: var(--ink);
  }
  .divider {
    position: absolute; left: 34px; top: 137px;
    width: 460px; height: 1.5px; background: var(--brand-red);
  }
  .holder-name {
    position: absolute; left: 34px; top: 82px;
    font-weight: 700; font-size: 21px; color: var(--brand-red);
  }
  .holder-title {
    position: absolute; left: 34px; top: 111px;
    font-size: 15px; color: var(--grey-text);
  }
  .contact-list {
    position: absolute; left: 34px; top: 160px;
    list-style: none; font-size: 14.5px; color: var(--grey-text);
  }
  .contact-list li { display: flex; align-items: center; gap: 12px; height: 26px; }
  .contact-list svg { width: 14px; height: 14px; flex: none; }
  .locations {
    position: absolute; right: 40px; top: 172px;
    font-size: 14px; line-height: 20px; color: var(--grey-text);
  }

  /* Back */
  .card-back {
    left: 625px;
    background: linear-gradient(125deg, var(--brand-red-deep) 0%, #b5171f 28%, var(--brand-red) 55%, var(--brand-red) 100%);
    color: var(--white);
  }
  .brand-back { position: absolute; left: 30px; top: 92px; }
  .brand-back .brand-name { color: var(--white); font-size: 38px; }
  .brand-tagline-back {
    display: block; margin-top: 4px;
    font-size: 11px; letter-spacing: 8px; color: var(--white);
  }
  .mission {
    position: absolute; left: 30px; top: 192px;
    font-size: 14px; line-height: 20px; text-transform: uppercase; letter-spacing: 0.3px;
  }
  .mission strong { font-style: italic; font-weight: 700; }
  .mission .mission-tail { text-transform: none; }
  .services {
    position: absolute; right: 30px; top: 80px;
    list-style: none; text-align: right;
    font-size: 14.5px; line-height: 23px;
  }
  .since-tag {
    position: absolute; right: 30px; top: 178px;
    background: var(--white); color: var(--brand-red);
    font-size: 15px; padding: 4px 12px 4px 18px;
    clip-path: polygon(12px 0, 100% 0, 100% 100%, 12px 100%, 0 50%);
  }
</style>
</head>
<body>
<main class="sheet">

  <section class="card card-front" aria-label="Business card front">
    <div class="brand-front">
      <span class="brand-mark" aria-hidden="true"></span>
      <span class="brand-name">Velmoro</span>
    </div>
    <div class="brand-tagline">CONSULTING</div>

    <h1 class="holder-name">Marlene Ostrander-Vale</h1>
    <p class="holder-title">CEO / Lead Project Manager</p>
    <div class="divider"></div>

    <ul class="contact-list">
      <li>
        <svg viewBox="0 0 24 24" aria-hidden="true"><path fill="#e41d27" d="M6.6 10.8a15.2 15.2 0 0 0 6.6 6.6l2.2-2.2a1 1 0 0 1 1-.25 11.4 11.4 0 0 0 3.6.57 1 1 0 0 1 1 1V20a1 1 0 0 1-1 1A17 17 0 0 1 3 4a1 1 0 0 1 1-1h3.5a1 1 0 0 1 1 1c0 1.25.2 2.45.57 3.57a1 1 0 0 1-.25 1z"/></svg>
        867.555.0193
      </li>
      <li>
        <svg viewBox="0 0 24 24" aria-hidden="true"><rect x="2.5" y="5" width="19" height="14" rx="1.5" fill="none" stroke="#e41d27" stroke-width="2.2"/><path d="M3 6l9 7 9-7" fill="none" stroke="#e41d27" stroke-width="2.2"/></svg>
        marlene@velmoro.ca
      </li>
      <li>
        <svg viewBox="0 0 24 24" aria-hidden="true"><circle cx="12" cy="12" r="9.5" fill="none" stroke="#e41d27" stroke-width="2"/><ellipse cx="12" cy="12" rx="4" ry="9.5" fill="none" stroke="#e41d27" stroke-width="1.6"/><path d="M2.5 12h19M4.5 7h15M4.5 17h15" stroke="#e41d27" stroke-width="1.6"/></svg>
        www.velmoro.ca
      </li>
    </ul>

    <p class="locations">Harrow Point NT<br>Lindell Bay NB</p>
  </section>

  <section class="card card-back" aria-label="Business card back">
    <div class="brand-back">
      <span class="brand-name">Velmoro</span>
      <span class="brand-tagline-back">CONSULTING</span>
    </div>

    <ul class="services">
      <li>FUNDING Planning</li>
      <li>BUSINESS Planning</li>
      <li>INFRASTRUCTURE Planning</li>
      <li>PROJECT Management</li>
    </ul>

    <span class="since-tag">Since 2012</span>

    <p class="mission">
      Execution<br>
      As the <strong>Owner's Rep</strong><br>
      We aim to achieve your<br>
      Infrastructure vision <span class="mission-tail">with</span><br>
      Our specialization &amp; execution <span class="mission-tail">in:</span>
    </p>
  </section>

</main>
</body>
</html>
```